Business card

We need a business card design for our company based in Auckland , New Zealand called 'Kestrel + Design Ltd'. We provide architectural services. We would like to see designs that use the max. three colours (such as white, black, grey) The final design should communicate financial safety and growth."
Also I will provide our company logo. I would like to the logo to be embeded onto our business card.

Target Market(s)

new residential house, alteration & addition & light commericila design & drafting service

Industry/Entity Type

Architecture

Contact Information for Business Card

Company name: kestrel + design Ltd.
Name: Mark Telford
Job title: architectural designer & Design RQC
email address: mark@kdstudio.co.nz
mobile number: 02 5319 6620
web site: www.kdstudio.co.nz

Requirements
Must have
• My project must have..
• - embeded logo (attached company logo)
• I don't have a bigger version for our company logo, but I have one old one, so you can remove the word from it)
• - insert the attached small PDGQ logo & RQC logo
• - creative, simple and clear business card.
• - Max. three colours
Nice to have
• - Here are the samples I would like to share with you: http://www.velmorindex.com/blog/minimalistic-business-card-designs/
• I would like to have my business card like one of the creation.
Should not have
• TBA

```html
<!DOCTYPE html>
<html lang="en">
<head>
<meta charset="utf-8">
<title>Kestrel + Design Ltd — Business Card</title>
<link href="https://fonts.googleapis.com/css2?family=Raleway:wght@400;500;800&display=swap" rel="stylesheet">
<style>
  :root {
    --charcoal: #3b3b3c;
    --paper: #f7f7f6;
    --white: #ffffff;
    --amber: #f0b632;
    --ink: #3a3a3a;
    --ink-soft: #6a6a6a;
    --backdrop: #e4e4e3;
  }
  * { margin: 0; padding: 0; box-sizing: border-box; }
  html, body {
    width: 1200px; height: 960px; overflow: hidden;
    background: var(--backdrop);
    font-family: "Raleway", sans-serif;
  }
  .sheet {
    position: relative; width: 1200px; height: 960px;
    display: flex; flex-direction: column; align-items: center; justify-content: center; gap: 60px;
  }
  .card {
    position: relative; width: 640px; height: 391px; overflow: hidden;
    box-shadow: 0 6px 18px rgba(0,0,0,0.12);
  }

  /* Logo side */
  .card--brand { background: var(--charcoal); }
  .tab { position: absolute; background: var(--amber); height: 26px; width: 120px; }
  .tab--top { left: 0; top: 0; }
  .tab--bottom { right: 0; bottom: 0; }
  .seal { position: absolute; border-radius: 50%; background: var(--white); }
  .card--brand .seal { width: 150px; height: 150px; left: 245px; top: 120px; }

  /* Contact side */
  .card--contact { background: var(--paper); }
  .panel { position: absolute; inset: 0; }

  .member { position: absolute; left: 34px; top: 30px; color: var(--white); }
  .member-name {
    display: flex; align-items: center; gap: 10px;
    font-size: 18px; font-weight: 500; letter-spacing: 1px;
  }
  .member-name .mark { width: 14px; height: 14px; background: var(--white); }
  .member-note {
    margin-top: 6px; font-size: 12px; font-weight: 500; line-height: 1.3; color: var(--white);
  }
  .card--contact .seal { width: 120px; height: 120px; left: 56px; top: 150px; }

  .identity { position: absolute; left: 318px; top: 96px; }
  .name { font-size: 34px; color: var(--ink); letter-spacing: 0.5px; }
  .name .first { font-weight: 800; }
  .name .last { font-weight: 400; }
  .role { margin-top: 6px; font-size: 15px; font-weight: 500; line-height: 1.35; color: var(--ink-soft); }

  .contacts { position: absolute; left: 262px; top: 196px; list-style: none; }
  .contacts li {
    display: flex; align-items: center; gap: 16px; height: 44px;
    font-size: 15px; font-weight: 500; color: var(--ink);
  }
  .contacts .icon {
    width: 32px; height: 32px; border-radius: 50%; background: var(--charcoal);
    display: flex; align-items: center; justify-content: center;
  }
  .rule { position: absolute; left: 262px; right: 28px; top: 340px; height: 3px; background: var(--amber); }
</style>
</head>
<body>
<main class="sheet">

  <section class="card card--brand" aria-label="Business card, logo side">
    <div class="tab tab--top"></div>
    <div class="tab tab--bottom"></div>
    <div class="seal" role="img" aria-label="RQC certification badge"></div>
  </section>

  <section class="card card--contact" aria-label="Business card, contact side">
    <svg class="panel" width="640" height="391" viewBox="0 0 640 391" aria-hidden="true">
      <polygon points="0,0 230,0 230,98 246,112 230,126 230,391 0,391" fill="var(--charcoal)"/>
      <rect x="230" y="200" width="24" height="96" fill="var(--amber)"/>
    </svg>

    <div class="member">
      <p class="member-name"><span class="mark" aria-hidden="true"></span>PDGQ</p>
      <p class="member-note">Professional<br>Member</p>
    </div>
    <div class="seal" role="img" aria-label="RQC certification badge"></div>

    <div class="identity">
      <h1 class="name"><span class="first">Mark</span> <span class="last">Telford</span></h1>
      <p class="role">Architectural Designer<br>&amp; Design RQC</p>
    </div>

    <ul class="contacts">
      <li>
        <span class="icon">
          <svg width="14" height="16" viewBox="0 0 14 16" aria-hidden="true">
            <rect x="2" y="0.8" width="10" height="14.4" rx="2" fill="none" stroke="#fff" stroke-width="1.6"/>
            <circle cx="7" cy="12.3" r="1" fill="#fff"/>
          </svg>
        </span>
        02 5319 6620
      </li>
      <li>
        <span class="icon">
          <svg width="16" height="12" viewBox="0 0 16 12" aria-hidden="true">
            <rect x="0.8" y="0.8" width="14.4" height="10.4" rx="1" fill="none" stroke="#fff" stroke-width="1.6"/>
            <polyline points="1,1.5 8,7 15,1.5" fill="none" stroke="#fff" stroke-width="1.6"/>
          </svg>
        </span>
        mark@kdstudio.co.nz
      </li>
      <li>
        <span class="icon">
          <svg width="16" height="16" viewBox="0 0 16 16" aria-hidden="true">
            <circle cx="8" cy="8" r="6.8" fill="none" stroke="#fff" stroke-width="1.4"/>
            <ellipse cx="8" cy="8" rx="3" ry="6.8" fill="none" stroke="#fff" stroke-width="1.2"/>
            <line x1="1.2" y1="8" x2="14.8" y2="8" stroke="#fff" stroke-width="1.2"/>
          </svg>
        </span>
        www.kdstudio.co.nz
      </li>
    </ul>

    <div class="rule"></div>
  </section>

</main>
</body>
</html>
```